NEW Website DESIGN for Brightwell Panes & Stoneworks Company

Brand New website, contemporary, clean, visual (images), not busy. ATTACHED IS OUR LOG THAT YOU MUST USE.

The company is called Brightwell Panes & Stoneworks (BrightwellPS)
www.brightwellps.com
The website should be www.brightwellpns.com
one page for glass one page for solid surfaces www.brightwellpanesplashes.co.uk
www.brightwellstoneworkss.co.uk

Target Market(s)

Hotels, Commercial projects, Small focus on residential

Industry/Entity Type

Construction

Number of Pages Required

5+ page

Font styles to use
Sans Serif

Requirements
Must have
• COLOURS AS PER OUR LOGO - WHITE/YELLOW/GREY - WHITE BACK GROUND
• CLEAR SIMPLE NAVIGATION - MODER CLEAN CUT - DESIGN FEEL
• LATEST NAVIGATION FOR IMAGES and text to include per project details
• WORK/PROJECT AREA - NEWS AREA - TEAM AREA/ABOUT US/CONTACT US
• NEW PAGEwww.brightwellpanesplashes.co.uk - NEW PAGE www.brightwellstoneworkss.co.uk
• PLEASE COPY THIS TYPE OF TEMPALTE
• https://www.harlowmead.co.uk/project/grand-halls/
• MOBILE READY
• WORDPRESS
• MODERN IMAGES INCLUDING VELMARA KESTRIN AND GLASS PROJECTS
Nice to have
• NEW DESIGN MODER FRESH
• WEBSITES I LIKE THE TEMPLATE SHOULD BE LIKE THE WEBSITE BELOW
• https://www.harlowmead.co.uk/
Should not have
• NOT Old fashion template, not busy NAVIGATION
• NO BLACK
• NO DARK GREYS
• NOT LOTS OF YELLOW
• RESDENTIAL IMAGES

```html
<!DOCTYPE html>
<html lang="en">
<head>
<meta charset="utf-8">
<title>Brightwell Panes &amp; Stoneworks</title>
<link rel="stylesheet" href="https://fonts.googleapis.com/css2?family=Orbitron:wght@700;800;900&family=Ubuntu:wght@400;500;700&display=swap">
<style>
:root{
  --orange:#e39b00;
  --orange-dark:#c98700;
  --cream:#fcefc9;
  --grey-dark:#4a4a4a;
  --grey-mid:#777;
  --grey-nav:#8a8a8a;
  --grey-light:#f4f4f4;
  --grey-line:#dedede;
  --footer:#333;
  --footer-nav:#575757;
  --text:#444;
  --white:#fff;
}
*{box-sizing:border-box;margin:0;padding:0}
html,body{width:1200px;height:3226px;overflow:hidden}
body{font-family:"Ubuntu",sans-serif;color:var(--text);background:var(--white);position:relative}
.display{font-family:"Orbitron",sans-serif;font-weight:800;text-transform:uppercase}
.btn{display:inline-block;background:var(--orange);color:var(--white);font:700 11px "Ubuntu",sans-serif;text-transform:uppercase;padding:9px 16px;border-radius:2px;letter-spacing:.3px}
.fill{position:absolute}
section,header,nav,footer{position:absolute;left:0;width:1200px}

/* header */
.site-header{top:0;height:103px;background:var(--white)}
.brand{position:absolute;left:200px;top:14px;display:flex;flex-direction:column;align-items:center;width:140px}
.brand-mark{width:50px;height:50px;border-radius:50%;background:var(--grey-mid)}
.brand-name{margin-top:6px;font:700 10px "Ubuntu",sans-serif;color:var(--grey-dark);text-align:center}
.header-slant{position:absolute;right:0;top:0}
.contact-block{position:absolute;left:570px;top:14px;display:flex;align-items:flex-start;gap:10px}
.phone-icon{width:30px;height:30px;border-radius:50%;background:var(--orange);margin-top:18px;display:flex;align-items:center;justify-content:center}
.contact-label{font:500 12px "Ubuntu",sans-serif;color:var(--grey-dark);letter-spacing:.5px}
.contact-phone{font:700 19px "Ubuntu",sans-serif;color:var(--orange);margin-top:3px}
.contact-email{font:400 11px "Ubuntu",sans-serif;color:var(--grey-dark)}
.social{position:absolute;left:806px;top:40px;display:flex;gap:6px}
.social span{width:30px;height:30px;background:var(--grey-nav);display:block}

.main-nav{top:103px;height:37px;background:var(--grey-nav)}
.main-nav ul{list-style:none;position:absolute;left:200px;top:0;display:flex;height:37px}
.main-nav li{font:700 11px "Ubuntu",sans-serif;color:var(--white);padding:0 24px;line-height:37px}
.main-nav li.active{background:var(--orange)}
.enquiry{position:absolute;left:870px;top:3px;height:31px;line-height:31px;padding:0 18px;background:var(--orange);color:var(--white);font:700 11px "Ubuntu",sans-serif}

/* hero */
.hero{top:140px;height:468px;background:linear-gradient(100deg,#d9d6d0 0%,#f2efe9 40%,#e4e0d8 70%,#c8c0a8 100%)}
.hero-panel{position:absolute;left:208px;top:97px;width:530px}
.hero-title{background:var(--orange);color:var(--white);padding:20px 30px 12px;font-size:33px;line-height:37px}
.hero-body{background:rgba(255,255,255,.88);padding:14px 30px 30px;position:relative}
.hero-body p{font-size:12.5px;line-height:19px;color:#333;margin-bottom:18px}
.hero-corner{position:absolute;right:0;bottom:0}
.hero-dots{position:absolute;left:576px;top:433px;display:flex;gap:4px}
.hero-dots i{width:9px;height:9px;background:rgba(255,255,255,.8);display:block}
.hero-dots i:first-child{background:var(--white)}

/* welcome */
.welcome{top:608px;height:417px;background:var(--grey-light)}
.welcome-text{position:absolute;left:208px;top:76px;width:426px}
.welcome-text h2{font-size:23px;line-height:24px;color:#333}
.welcome-text h2 small{font-size:18px;display:block}
.welcome-text p{font-size:11.5px;line-height:19px;color:#555;margin-top:16px}
.welcome-art{position:absolute;left:640px;top:40px}
.welcome-photo{left:666px;top:72px;width:312px;height:270px;background:linear-gradient(160deg,#f4f4f6 0%,#c9c9d0 45%,#c8306c 60%,#a01e50 75%,#e6e6ea 100%);border:3px solid var(--white)}

/* work */
.work{top:1025px;height:555px;background:var(--white)}
.section-title{font-size:26px;text-align:center;color:#333;font-weight:800}
.work .section-title{position:absolute;top:48px;width:100%}
.work-grid{position:absolute;left:208px;top:108px;display:flex;gap:8px}
.work-card{width:194px;height:387px;background:var(--white);box-shadow:0 1px 4px rgba(0,0,0,.15);text-align:center}
.work-img{height:126px}
.work-card h3{font:500 13px "Ubuntu",sans-serif;color:#333;text-transform:uppercase;margin:22px 12px 14px;line-height:17px}
.work-card p{font-size:11px;line-height:17px;color:#555;margin:0 20px 16px}

/* estimates */
.estimates{top:1580px;height:130px;background:var(--cream)}
.estimates-img{left:0;top:0;width:420px;height:130px;background:linear-gradient(120deg,#d8dcd6,#b8c8c0 50%,#6aa8a0 100%)}
.estimates-curve{position:absolute;left:330px;top:0}
.estimates h2{position:absolute;left:443px;top:32px;font-size:20px;color:#333}
.estimates p{position:absolute;left:443px;top:66px;width:400px;font-size:11.5px;line-height:17px;color:#555}
.estimates .btn{position:absolute;left:877px;top:44px;border:2px solid rgba(255,255,255,.6)}

/* team */
.team{top:1710px;height:462px;background:var(--white)}
.team-title{position:absolute;top:52px;left:208px;width:784px;display:flex;align-items:center;gap:22px}
.team-title::before,.team-title::after{content:"";flex:1;height:2px;background:var(--orange)}
.team-title h2{font-size:26px;color:#333}
.team-grid{position:absolute;left:208px;top:118px;display:flex;gap:19px}
.member{width:181px;height:247px;position:relative;background:linear-gradient(180deg,#cfcfcf,#9a9a9a)}
.member-caption{position:absolute;left:0;bottom:0;width:100%;height:54px;background:rgba(120,120,120,.9);padding:10px 12px;color:var(--white)}
.member-caption b{font:500 12px "Ubuntu",sans-serif;display:block}
.member-caption span{font-size:9px}
.team .btn{position:absolute;left:544px;top:384px}

/* news & reviews */
.stories{top:2172px;height:391px;background:var(--white)}
.news{position:absolute;left:200px;top:26px;width:370px}
.news-head{display:flex;justify-content:space-between;align-items:center;border-bottom:2px solid var(--orange);padding-bottom:8px}
.news-head h2{font-size:22px;color:#333}
.news-head .btn{padding:6px 12px;font-size:10px}
.news-item{display:flex;gap:16px;margin-top:20px}
.news-thumb{width:133px;height:82px;flex:none}
.news-meta{font-size:9px;color:#777}
.news-cat{font-size:9.5px;color:var(--orange);margin-top:8px}
.news-item h3{font:400 13.5px "Ubuntu",sans-serif;color:#333;line-height:18px;margin-top:3px}
.reviews{position:absolute;left:606px;top:0;width:594px;height:391px;background:linear-gradient(90deg,#f0f0ee 0%,#ecebe8 45%,#d7d2c9 75%,#c4b8a6 100%)}
.reviews h2{position:absolute;left:26px;top:24px;font-size:23px;line-height:24px;color:#333}
.quote{position:absolute;left:22px;top:110px;width:330px}
.quote p{font-size:11.5px;line-height:24px;color:#555;padding-left:30px;padding-right:20px}
.quote cite{display:block;font-style:normal;font-size:11.5px;color:#555;margin-top:14px;padding-left:30px}
.quote-mark{position:absolute;font:900 34px "Ubuntu",sans-serif;color:var(--orange);line-height:1}
.review-dots{position:absolute;left:52px;top:328px;display:flex;gap:4px}
.review-dots i{width:9px;height:9px;border-radius:50%;background:#ccc;display:block}
.review-dots i:first-child{background:var(--orange)}

/* contact */
.contact{top:2563px;height:387px;background:#e2e2e2}
.map{left:208px;top:0;width:422px;height:387px;background:linear-gradient(135deg,#eef0ea 0%,#e4e8e0 50%,#f0ede2 100%)}
.map-card{position:absolute;left:270px;top:155px;width:176px;height:78px;background:var(--orange);color:var(--white);padding:14px 10px;font-size:9.5px;line-height:14px}
.map-pin{position:absolute;left:440px;top:148px;width:78px;height:78px;border-radius:50%;background:var(--white);border:3px solid var(--orange);display:flex;align-items:center;justify-content:center}
.map-pin span{width:44px;height:44px;border-radius:50%;background:var(--grey-mid);display:block}
.quote-form{position:absolute;left:630px;top:0;width:362px;height:387px;background:var(--white);border:5px solid var(--grey-dark)}
.quote-form h2{background:var(--grey-dark);color:var(--white);font-size:15px;padding:14px 30px 18px}
.quote-form form{padding:12px 40px 0}
.field{height:34px;border:1px solid var(--grey-line);margin-bottom:8px;font-size:10px;color:#666;padding:10px 12px}
.field.area{height:80px}
.quote-form .btn{margin-top:12px;padding:12px 20px}
.form-corner{position:absolute;right:0;bottom:0}

/* footer */
.footer-nav{top:2950px;height:50px;background:var(--footer-nav)}
.footer-nav ul{list-style:none;position:absolute;left:310px;display:flex;gap:0}
.footer-nav li{font:500 11px "Ubuntu",sans-serif;color:var(--white);width:104px;text-align:center;line-height:50px}
.site-footer{top:3000px;height:226px;background:var(--footer);color:var(--white)}
.foot-col{position:absolute;top:42px;width:240px;text-align:center}
.foot-col h3{font:500 15px "Ubuntu",sans-serif;display:flex;justify-content:center;align-items:center;gap:8px;padding-bottom:10px;border-bottom:1px solid #666}
.foot-col p{font-size:11px;line-height:18px;margin-top:12px}
.foot-phone{font:500 18px "Ubuntu",sans-serif;margin-top:16px}
.foot-brand{position:absolute;left:480px;top:18px;width:240px;text-align:center}
.foot-brand .brand-mark{margin:0 auto;width:66px;height:66px;background:#ddd}
.foot-brand .brand-name{color:var(--white);font-size:12px;margin-top:8px}
.foot-social{display:flex;justify-content:center;gap:6px;margin-top:10px}
.foot-social span{width:30px;height:30px;background:var(--white);display:block}
.copyright{position:absolute;left:0;top:194px;width:100%;text-align:center;font-size:10px;color:#ddd}
</style>
</head>
<body>

<header class="site-header">
  <svg class="header-slant" width="340" height="103" viewBox="0 0 340 103"><polygon points="300,0 340,0 340,103 250,103" fill="#f1f1f1"/></svg>
  <div class="brand">
    <span class="brand-mark"></span>
    <span class="brand-name">Brightwell Panes &amp; Stoneworks</span>
  </div>
  <div class="contact-block">
    <span class="phone-icon"><svg width="14" height="14" viewBox="0 0 24 24"><path fill="#fff" d="M6.6 10.8a15 15 0 0 0 6.6 6.6l2.2-2.2a1 1 0 0 1 1-.25 11.4 11.4 0 0 0 3.6.57 1 1 0 0 1 1 1V20a1 1 0 0 1-1 1A17 17 0 0 1 3 4a1 1 0 0 1 1-1h3.5a1 1 0 0 1 1 1c0 1.25.2 2.45.57 3.57a1 1 0 0 1-.25 1z"/></svg></span>
    <div>
      <div class="contact-label">CONTACT US NOW</div>
      <div class="contact-phone">+44 (0)1632 960 548</div>
      <div class="contact-email">sales@brightwellpanesplashes.co.uk</div>
    </div>
  </div>
  <div class="social"><span></span><span></span><span></span><span></span></div>
</header>

<nav class="main-nav">
  <ul>
    <li class="active">HOME</li><li>WORK</li><li>ABOUT</li><li>NEWS</li><li>TEAM</li><li>CONTACT</li>
  </ul>
  <div class="enquiry">ENQUIRY FORM</div>
</nav>

<section class="hero" role="img" aria-label="Photo of a bright modern kitchen with glass splashbacks and a bamboo plant">
  <div class="hero-panel">
    <h1 class="hero-title display">Glass Splashbacks<br>Designed By You</h1>
    <div class="hero-body">
      <p>We supply and fit any bespoke Velmara and glass products to our clients' specification, shape, finish and colour: you imagine it, and we will help make it a reality. Crisp, clean and modern, they are the ultimate complement to the contemporary home or business.</p>
      <span class="btn">Get in touch for a quote</span>
      <svg class="hero-corner" width="40" height="40" viewBox="0 0 40 40"><polygon points="40,0 40,40 0,40" fill="#4a4a4a"/></svg>
    </div>
  </div>
  <div class="hero-dots"><i></i><i></i><i></i><i></i><i></i></div>
</section>

<section class="welcome">
  <div class="welcome-text">
    <h2 class="display"><small>Welcome to</small>Brightwell Panes</h2>
    <p>Lorem ipsum dolor sit amet, consectetur adipiscing elit, sed do eiusmod tempor incididunt ut labore et dolore magna aliqua. Ut enim ad minim veniam, quis nostrud exercitation ullamco laboris nisi ut aliquip ex ea commodo consequat. Duis aute irure dolor in reprehenderit in voluptate velit esse cillum dolore eu fugiat nulla pariatur. Excepteur sint occaecat cupidatat non proident, sunt in culpa qui officia deserunt mollit anim id est laborum.</p>
    <p>Sed ut perspiciatis unde omnis iste natus error sit voluptatem accusantium doloremque laudantium, totam rem aperiam, eaque ipsa quae ab illo inventore veritatis et quasi architecto beatae vitae dicta sunt explicabo. consequuntur magni dolores eos qui ratione voluptatem sequi nesciunt.</p>
  </div>
  <svg class="welcome-art" width="360" height="370" viewBox="0 0 360 370">
    <polygon points="130,0 170,0 150,45 110,45" fill="#e39b00"/>
    <polygon points="180,0 220,0 200,45 160,45" fill="#f0b830"/>
    <polygon points="230,20 330,20 330,60 210,60" fill="#e39b00"/>
    <polygon points="330,60 345,60 345,300 330,300" fill="#e39b00"/>
    <polygon points="60,300 120,300 100,350 40,350" fill="#e39b00"/>
    <polygon points="130,300 190,300 170,350 110,350" fill="#f0b830"/>
    <polygon points="200,300 250,300 230,350 180,350" fill="#f5c95a"/>
  </svg>
  <div class="fill welcome-photo" role="img" aria-label="Photo of a white kitchen with a magenta glass splashback"></div>
</section>

<section class="work">
  <h2 class="section-title display">Our Work</h2>
  <div class="work-grid">
    <article class="work-card">
      <div class="work-img" role="img" aria-label="Photo of a kitchen with a pink splashback" style="background:linear-gradient(160deg,#eee,#c23a72 55%,#ddd)"></div>
      <h3>Bespoke Velmara</h3>
      <p>Kestrin™ Velmara® is becoming the workhorse of choice among trade professionals, customer-facing businesses and home-owners in the know. It is versatile.</p>
      <span class="btn">Read more</span>
    </article>
    <article class="work-card">
      <div class="work-img" role="img" aria-label="Photo of a kitchen with green glass worktops" style="background:linear-gradient(160deg,#f1f1ee,#a9cfc3 55%,#e7e7e3)"></div>
      <h3>Contemporary glass worktops and splashbacks</h3>
      <p>A bespoke glass worktop or splashback, from Brightwell Panes, creates a distinctive designer style in any room be it in a home, business or commercial.</p>
      <span class="btn">Read more</span>
    </article>
    <article class="work-card">
      <div class="work-img" role="img" aria-label="Photo of a bathroom with large mirrors" style="background:linear-gradient(160deg,#f5f5f5,#8a7a6c 55%,#e8e8e8)"></div>
      <h3>Beautiful mirrors</h3>
      <p>Manufactured in house we have a vast range of mirror frames to suit all styles from modern to contemporary. Bathrooms mirrors are turned around quickly.</p>
      <span class="btn">Read more</span>
    </article>
    <article class="work-card">
      <div class="work-img" role="img" aria-label="Photo of a wet room with a glass shower enclosure" style="background:linear-gradient(160deg,#d8d8d8,#8c8c8c 55%,#cfcfcf)"></div>
      <h3>Wet rooms</h3>
      <p>Because everything is manufactured in house, we can create glass shower enclosures for any size of bathroom or wet room. Made bespoke for your project.</p>
      <span class="btn">Read more</span>
    </article>
  </div>
</section>

<section class="estimates">
  <div class="fill estimates-img" role="img" aria-label="Photo of a kitchen counter with a green glass worktop"></div>
  <svg class="estimates-curve" width="100" height="130" viewBox="0 0 100 130"><path d="M60 0 Q20 65 0 130 L100 130 L100 0 Z" fill="#fcefc9"/><path d="M60 0 Q20 65 0 130 L14 130 Q34 65 74 0 Z" fill="#e39b00"/></svg>
  <h2 class="display">Get your free estimates</h2>
  <p>Lorem ipsum dolor sit amet, consectetur adipiscing elit, sed do eiusmod tempor incididunt ut labore et dolore magna aliqua.</p>
  <span class="btn">Contact us</span>
</section>

<section class="team">
  <div class="team-title"><h2 class="display">Meet our team</h2></div>
  <div class="team-grid">
    <div class="member" role="img" aria-label="Portrait photo of team member Tom Reyes"><div class="member-caption"><b>Tom Reyes</b><span>Sales lead</span></div></div>
    <div class="member" role="img" aria-label="Portrait photo of team member Sam Adley"><div class="member-caption"><b>Sam Adley</b><span>Fitter</span></div></div>
    <div class="member" role="img" aria-label="Portrait photo of team member Jerry Tolan"><div class="member-caption"><b>Jerry Tolan</b><span>Designer</span></div></div>
    <div class="member" role="img" aria-label="Portrait photo of team member Alan Smythe"><div class="member-caption"><b>Alan Smythe</b><span>Director</span></div></div>
  </div>
  <span class="btn">Meet our team</span>
</section>

<section class="stories">
  <div class="news">
    <div class="news-head"><h2 class="display">Latest news</h2><span class="btn">View all</span></div>
    <div class="news-item">
      <div class="news-thumb" role="img" aria-label="Photo of an office building among trees" style="background:linear-gradient(135deg,#6f8a5a,#c9d3c0)"></div>
      <div><div class="news-meta">04 AUG, 2018 | BPS ADMIN</div><div class="news-cat">About Us</div><h3>Spotlight on ... our virtual office!</h3></div>
    </div>
    <div class="news-item">
      <div class="news-thumb" role="img" aria-label="Photo of a kitchen with glass worktops" style="background:linear-gradient(135deg,#555,#bdb8b0)"></div>
      <div><div class="news-meta">02 AUG, 2018 | BPS ADMIN</div><div class="news-cat">Throwback Thursday</div><h3>Glass Worktops in record time!</h3></div>
    </div>
    <div class="news-item">
      <div class="news-thumb" role="img" aria-label="Purple awareness ribbon" style="background:linear-gradient(135deg,#f3f0f5,#cbb8d8)"></div>
      <div><div class="news-meta">02 AUG, 2018 | BPS ADMIN</div><div class="news-cat">Charity</div><h3>Fundraising for little Ellie-May who has Cystic Fibrosis</h3></div>
    </div>
  </div>
  <div class="reviews" role="img" aria-label="Photo of a smiling family in a bright living room">
    <h2 class="display">Happy customer<br>reviews</h2>
    <div class="quote">
      <span class="quote-mark" style="left:0;top:2px">“</span>
      <p>Lorem ipsum dolor sit amet, consectetur adipiscing elit, sed do eiusmod tempor incididunt ut labore et dolore magna aliqua. Ut enim ad minim veniam, quis nostrud exercitation ullamco laboris nisi ut aliquip ex ea commodo consequat. Duis aute irure dolor in reprehenderit in voluptate velit esse cillum dolore eu fugiat nulla pariatur.</p>
      <span class="quote-mark" style="right:4px;top:196px">”</span>
      <cite>- Sam Adley</cite>
    </div>
    <div class="review-dots"><i></i><i></i><i></i><i></i><i></i></div>
  </div>
</section>

<section class="contact">
  <div class="fill map" role="img" aria-label="Street map showing the business centre location"></div>
  <div class="map-card">Larkfield Business Centre<br>Mill Road, Ashcombe<br>AC4 0WS</div>
  <div class="map-pin"><span></span></div>
  <div class="quote-form">
    <h2 class="display">Get in touch for a quote</h2>
    <form>
      <div class="field">Your Name</div>
      <div class="field">Your Email Address</div>
      <div class="field">Your Phone Number</div>
      <div class="field area">Your Message</div>
      <span class="btn">Send us a message</span>
    </form>
    <svg class="form-corner" width="30" height="30" viewBox="0 0 30 30"><polygon points="30,0 30,30 0,30" fill="#4a4a4a"/></svg>
  </div>
</section>

<nav class="footer-nav">
  <ul><li>HOME</li><li>WORK</li><li>ABOUT</li><li>NEWS</li><li>TEAM</li><li>CONTACT</li></ul>
</nav>

<footer class="site-footer">
  <div class="foot-col" style="left:200px">
    <h3><svg width="12" height="16" viewBox="0 0 12 16"><path d="M6 0a6 6 0 0 0-6 6c0 4.5 6 10 6 10s6-5.5 6-10a6 6 0 0 0-6-6zm0 8.5A2.5 2.5 0 1 1 6 3.5a2.5 2.5 0 0 1 0 5z" fill="#fff"/></svg>OUR LOCATION</h3>
    <p>Larkfield Business Centre<br>Mill Road, Ashcombe<br>AC4 0WS</p>
  </div>
  <div class="foot-brand">
    <span class="brand-mark"></span>
    <div class="brand-name">Brightwell Panes &amp; Stoneworks</div>
    <div class="foot-social"><span></span><span></span><span></span><span></span></div>
  </div>
  <div class="foot-col" style="left:760px">
    <h3><svg width="14" height="14" viewBox="0 0 24 24"><path fill="#fff" d="M6.6 10.8a15 15 0 0 0 6.6 6.6l2.2-2.2a1 1 0 0 1 1-.25 11.4 11.4 0 0 0 3.6.57 1 1 0 0 1 1 1V20a1 1 0 0 1-1 1A17 17 0 0 1 3 4a1 1 0 0 1 1-1h3.5a1 1 0 0 1 1 1c0 1.25.2 2.45.57 3.57a1 1 0 0 1-.25 1z"/></svg>PHONE</h3>
    <div class="foot-phone">+44 (0)1632 960 548</div>
  </div>
  <div class="copyright">© 2018 Brightwell Panes &amp; Stoneworks</div>
</footer>

</body>
</html>
```